Stationery Design Project

Brisk-Span Consultants is interim management company. We are specialized in finding the best Finance and IT consultants for our clients when they require additional resources on an interim basis for projects or special situations. We are flexible in our approach and we always seek to maximize the benefits for our clients as well as our consultants.

We are looking for a design of our letterhead, general stationery and business cards using the company name. The design will also be found on our coming web pages.
Updates

Please also create a logo for Brisk-Span Consultants which expresses that we want to match the best finance and IT people to our customers projects

Target Market(s)

Larger and mid sized companies (all sectors), as well as highly skilled Finance & IT professionals/consultants

Industry/Entity Type

Business

Requirements
Must have
• Brisk-Span Consultants
We are expecting that 'Brisk-Span' will be on the first line and 'Consultants' on a second line.
Please also indicate style of the letters for our address/phone and mail details. Our current address is:
Tornagervej 14,
2915 Skovlunde
Danmark
Mobile: +45 XX XX XX XX Mail: xx@brisk-span.dk

```html
<!DOCTYPE html>
<html lang="en">
<head>
<meta charset="utf-8">
<title>Brisk-Span Consultants – Stationery</title>
<link rel="stylesheet" href="https://fonts.googleapis.com/css2?family=Arimo:ital,wght@0,400;0,700;1,400&display=swap">
<style>
  :root {
    --brand-dark: #1b3f98;
    --brand-mid: #5a7bbf;
    --brand-text: #5b78c4;
    --paper: #ffffff;
    --edge: #b9c3cc;
    --shadow: rgba(60, 70, 90, 0.28);
    --backdrop: #ffffff;
  }
  * { box-sizing: border-box; margin: 0; padding: 0; }
  html, body {
    width: 1200px; height: 900px; overflow: hidden;
    background: var(--backdrop);
    font-family: "Arimo", Arial, sans-serif;
  }
  .canvas { position: relative; width: 1200px; height: 900px; }

  .sheet {
    position: absolute;
    background: var(--paper);
    border: 1px solid var(--edge);
    box-shadow: 6px 6px 8px var(--shadow);
    overflow: hidden;
  }

  /* Wordmark */
  .wordmark {
    position: absolute;
    display: flex; align-items: center; gap: 10px;
    color: var(--brand-dark);
    font-weight: 400;
  }
  .wordmark__square { width: 30px; height: 30px; background: currentColor; flex: none; }
  .wordmark__text { display: flex; flex-direction: column; line-height: 1; }
  .wordmark__name { font-size: 29px; letter-spacing: -0.5px; }
  .wordmark__sub { font-size: 11px; letter-spacing: 5.6px; margin-top: 1px; }
  .wordmark--light { color: #ffffff; }

  .corner-block { position: absolute; }

  /* Letterhead */
  .letterhead { left: 73px; top: 25px; width: 585px; height: 804px; }
  .letterhead .corner-block { left: 0; top: 0; width: 90px; height: 90px; background: var(--brand-mid); }
  .letterhead .wordmark { right: 44px; top: 34px; }
  .letterhead__contact {
    position: absolute; right: 38px; top: 92px;
    text-align: right; font-style: italic; font-size: 11.5px; line-height: 15px;
    color: var(--brand-text); white-space: pre;
  }
  .letterhead__footer-mark {
    position: absolute; left: 271px; top: 754px;
    width: 30px; height: 30px; background: var(--brand-dark);
  }

  /* Business cards */
  .card { width: 266px; height: 162px; }
  .card--logo-dark { left: 684px; top: 73px; background: var(--brand-dark); border-color: var(--brand-dark); }
  .card--details-light { left: 833px; top: 227px; }
  .card--logo-light { left: 684px; top: 465px; }
  .card--details-mid { left: 833px; top: 620px; background: var(--brand-mid); border-color: var(--brand-mid); }

  .card .wordmark { left: 28px; top: 58px; }
  .card .wordmark__square { width: 24px; height: 24px; }
  .card .wordmark__name { font-size: 24px; }
  .card .wordmark__sub { font-size: 9px; letter-spacing: 4.6px; }

  .card--details-light .corner-block { left: 0; top: 8px; width: 62px; height: 62px; background: var(--brand-mid); }
  .card--details-mid .corner-block { right: 0; top: 0; width: 92px; height: 92px; background: var(--brand-dark); }

  .contact-card { position: absolute; color: var(--brand-dark); }
  .contact-card__name { font-weight: 700; font-size: 12.5px; line-height: 14px; }
  .contact-card__role {
    font-weight: 700; font-size: 6.5px; text-align: right; letter-spacing: 0.3px;
    margin-top: 1px; width: 82px;
  }
  .contact-card__details {
    margin-top: 10px; font-style: italic; font-size: 9.5px; line-height: 11.8px;
    color: var(--brand-text); white-space: pre;
  }
  .card--details-light .contact-card { left: 77px; top: 42px; }
  .card--details-mid .contact-card { left: 100px; top: 40px; color: #ffffff; }
  .card--details-mid .contact-card__details { color: #ffffff; }
</style>
</head>
<body>
<main class="canvas">

  <section class="sheet letterhead" aria-label="Letterhead">
    <div class="corner-block"></div>
    <div class="wordmark">
      <span class="wordmark__square"></span>
      <span class="wordmark__text">
        <span class="wordmark__name">BRISK-SPAN</span>
        <span class="wordmark__sub">CONSULTANTS</span>
      </span>
    </div>
    <p class="letterhead__contact">Tornagervej 14  .  2915 Skovlunde  .  Danmark
Mobile: +45 31 62 47 85  .  Mail: MK@brisk-span.dk</p>
    <div class="letterhead__footer-mark"></div>
  </section>

  <section class="sheet card card--logo-dark" aria-label="Business card front, dark">
    <div class="wordmark wordmark--light">
      <span class="wordmark__square"></span>
      <span class="wordmark__text">
        <span class="wordmark__name">BRISK-SPAN</span>
        <span class="wordmark__sub">CONSULTANTS</span>
      </span>
    </div>
  </section>

  <section class="sheet card card--details-light" aria-label="Business card back, light">
    <div class="corner-block"></div>
    <div class="contact-card">
      <p class="contact-card__name">Mads Kjeldgaard</p>
      <p class="contact-card__role">DIRECTOR</p>
      <p class="contact-card__details">Tornagervej 14,
2915 Skovlunde
Danmark
Mobile: +45 31 62 47 85
Mail: MK@brisk-span.dk</p>
    </div>
  </section>

  <section class="sheet card card--logo-light" aria-label="Business card front, light">
    <div class="wordmark">
      <span class="wordmark__square"></span>
      <span class="wordmark__text">
        <span class="wordmark__name">BRISK-SPAN</span>
        <span class="wordmark__sub">CONSULTANTS</span>
      </span>
    </div>
  </section>

  <section class="sheet card card--details-mid" aria-label="Business card back, blue">
    <div class="corner-block"></div>
    <div class="contact-card">
      <p class="contact-card__name">Mads Kjeldgaard</p>
      <p class="contact-card__role">DIRECTOR</p>
      <p class="contact-card__details">Tornagervej 14,
2915 Skovlunde
Danmark
Mobile: +45 31 62 47 85
Mail: MK@brisk-span.dk</p>
    </div>
  </section>

</main>
</body>
</html>
```